Austrian finance und insurance broker needs business card design

We Need a serious looking Design for Business Card. we consult private and corporates customers in finance and insurance questions. the final design should express security and experience. We consult customers in questions of loans, Investments and insurance and have a wide range of Banks to offer. We compare several offers and select the best for our customers.

Target Market(s)

private and coporate customers with efforts in Money and insurance

Industry/Entity Type

Insurance Broker

Contact Information for Business Card

Bernhard Aigner
Geschäftsführer
staatl. geprüfter Vermögensberater und Versicherungsmakler
Tel: 0664 521 8409
office@der-brandl.at
www.der-brandl.at
Leopold Hainz Gasse 14
2183 Melkstetten
GISA Nr. 48270315 u. 51736048 (backside)

Font styles to use
Serif
Sans Serif

Requirements
Must have
• logo (designcrowd zip) and all Details
Nice to have
• makler logo design, maybe a 2 coloured Version is possible

```html
<!DOCTYPE html>
<html lang="de">
<head>
<meta charset="utf-8">
<title>Visitenkarte – Bernhard Aigner</title>
<link rel="stylesheet" href="https://fonts.googleapis.com/css2?family=Open+Sans:wght@300;400;600&family=Nunito:wght@600;700&display=swap">
<style>
  :root {
    --backdrop: #1e1e1e;
    --card-white: #ffffff;
    --card-blue: #2b5ca8;
    --brand-blue: #2356b0;
    --text-grey: #555a60;
    --text-light: #ffffff;
    --badge-red: #c62638;
    --icon-red: #e0323c;
    --icon-cyan: #22a6dc;
  }
  * { box-sizing: border-box; margin: 0; padding: 0; }
  html, body { width: 1200px; height: 1003px; overflow: hidden; }
  body {
    background: var(--backdrop);
    display: flex; align-items: center; justify-content: center; gap: 70px;
    font-family: "Open Sans", sans-serif;
  }
  .card {
    width: 380px; height: 600px; position: relative;
    box-shadow: 0 10px 30px rgba(0,0,0,.5);
  }
  /* Front */
  .card-front { background: var(--card-white); }
  .partner-badge {
    position: absolute; top: 22px; right: 22px;
    width: 46px; height: 46px; border-radius: 50%; background: var(--badge-red);
  }
  .brand {
    position: absolute; left: 36px; right: 24px; top: 262px;
    display: flex; align-items: center; gap: 14px;
  }
  .brand-circle {
    width: 72px; height: 72px; flex: none; border-radius: 50%;
    border: 4px solid var(--brand-blue);
  }
  .brand-name {
    font-family: "Nunito", sans-serif; font-weight: 700;
    color: var(--brand-blue); font-size: 19px; line-height: 1.15;
  }
  .brand-tagline {
    font-family: "Nunito", sans-serif; font-weight: 600;
    color: var(--text-grey); font-size: 12.5px; margin-top: 5px;
  }
  /* Back */
  .card-back {
    background: var(--card-blue); color: var(--text-light);
    text-align: center; padding: 86px 24px 0;
  }
  .person-name { font-weight: 400; font-size: 23px; letter-spacing: .5px; }
  .person-role { font-weight: 300; font-size: 17px; margin-top: 2px; }
  .qualification { font-weight: 300; font-size: 16.5px; line-height: 1.45; margin-top: 44px; }
  .divider-row {
    display: flex; align-items: center; justify-content: center; gap: 10px;
    margin-top: 30px;
  }
  .divider-row .rule { width: 58px; height: 1px; background: rgba(255,255,255,.7); }
  .icon { width: 24px; height: 24px; border-radius: 50%; display: inline-flex;
    align-items: center; justify-content: center; background: var(--text-light); }
  .icon-mail { background: var(--icon-red); }
  .icon-chat { background: var(--icon-cyan); }
  .icon-social { background: transparent; border: 1.5px solid var(--text-light); }
  .contact { margin-top: 14px; font-weight: 300; font-size: 17px; line-height: 1.4; }
  .contact .phone { font-weight: 400; font-size: 19px; }
  .address { margin-top: 22px; font-weight: 300; font-size: 15.5px; line-height: 1.7; }
</style>
</head>
<body>
  <section class="card card-front">
    <div class="partner-badge" role="img" aria-label="Partnerabzeichen"></div>
    <div class="brand">
      <div class="brand-circle"></div>
      <div>
        <div class="brand-name">Aigner Vermögensberatung GmbH</div>
        <div class="brand-tagline">Finanzieren, Versichern, Vorsorgen</div>
      </div>
    </div>
  </section>

  <section class="card card-back">
    <h1 class="person-name">BERNHARD AIGNER</h1>
    <p class="person-role">Geschäftsführer</p>
    <p class="qualification">Staatl. Geprüfter Vermögensberater und<br>Versicherungsmakler</p>

    <div class="divider-row">
      <span class="rule"></span>
      <span class="icon" aria-label="Telefon">
        <svg width="14" height="14" viewBox="0 0 24 24"><path fill="#2b5ca8" d="M6.6 10.8a15 15 0 0 0 6.6 6.6l2.2-2.2c.3-.3.7-.4 1-.2 1.1.4 2.3.6 3.6.6.6 0 1 .4 1 1V20c0 .6-.4 1-1 1A17 17 0 0 1 3 4c0-.6.4-1 1-1h3.5c.6 0 1 .4 1 1 0 1.3.2 2.5.6 3.6.1.3 0 .7-.2 1z"/></svg>
      </span>
      <span class="icon icon-mail" aria-label="E-Mail">
        <svg width="14" height="10" viewBox="0 0 14 10"><rect x=".5" y=".5" width="13" height="9" fill="none" stroke="#fff"/><path d="M.5 .5 7 6l6.5-5.5" fill="none" stroke="#fff"/></svg>
      </span>
      <span class="icon icon-chat"></span>
      <span class="icon icon-social"></span>
      <span class="rule"></span>
    </div>

    <div class="contact">
      <div class="phone">0664 521 8409</div>
      <div>office@der-brandl.at</div>
      <div>www.der-brandl.at</div>
    </div>

    <div class="divider-row">
      <span class="rule"></span>
      <span class="icon" aria-label="Adresse">
        <svg width="12" height="16" viewBox="0 0 12 16"><path fill="#2b5ca8" d="M6 0a6 6 0 0 0-6 6c0 4.5 6 10 6 10s6-5.5 6-10a6 6 0 0 0-6-6zm0 8.5A2.5 2.5 0 1 1 6 3.5a2.5 2.5 0 0 1 0 5z"/></svg>
      </span>
      <span class="rule"></span>
    </div>

    <div class="address">
      <div>Leopold Hainz Gasse 14, 2183 Melkstetten</div>
      <div>GISA Nr. 48270315 u. 51736048 (backside)</div>
    </div>
  </section>
</body>
</html>
```